Edible Insect Sticker packaging design

The successful designer for this product will be hired again for more packaging design products in this product range.
We are a company that manufactures edible insects and we have some new products coming out we ned packaging for. As you can imagine the stickers are very small 50mm x 50mm.
Each sticker design will be in a set  of 2 (one for the front and one for the back of the packaging).
The front will contain the weight of the product (in grams) as well as the name of the product and design.
The back will contain our company logo and info as well as NIP (Nutritional Information Panel), ingredient declaration, and 3-4 lines of information about how edible insects are great for the environment.
At this stage I would like the packaging to have a slightly environmental free, but still colourful and eye catching. I am open to any suggestions for the design though if you have some great ideas!
Must also contain the slogan (on front or back), "Are you Brave Enough?"
There are several products in the range, and would like the labels to be in a set. Basic lay out will be the same for each product, and the front sticker will be slightly different.
Products are
Zib-A-Lop Tundle- a fly shaped chocolate that contains coconut and fly pupae
Plinky Pebbles- 5 x roasted crickets
Tootle Twirlies- 5 x roasted mealworms
Fudge Dipped Fidgets- 5 x insects, chocolate coated in milk, white or dark chocolate. Insects include crickets, mealworms and fly pupae
Specific information (eg, NIP, ingredients etc) will be sent to chosen designer to add to the deisgn.
Attached is image of 3 products (Zib-A-Lop Tundle, roasted mealworms and roasted crickets) as well as logo. The chocolate coated bugs are the 2 types of roasted bugs pictured in the attachment coated in chocolate.

Updates
Design can be square or round 

Reason: Several designers have asked for an extension to submit new/ revised designs.

Reason: I have extended the deadline by one day to allow for revisions and new designs to be submitted.

```html
<!DOCTYPE html>
<html lang="en">
<head>
<meta charset="utf-8">
<title>Critter Pantry – Front Label Set</title>
<link href="https://fonts.googleapis.com/css2?family=Open+Sans:wght@700;800&family=Ubuntu:wght@300&display=swap" rel="stylesheet">
<style>
  :root {
    --lime: #9dc137;
    --olive: #7f7d39;
    --rust: #86503a;
    --cocoa: #4c271a;
    --paper: #ffffff;
    --ink: #1c1c1c;
    --muted-ink: #333333;
    --divider: #6a6a6a;
    --brand: #8a8b3c;
    --headline-font: "Open Sans", Arial, sans-serif;
    --body-font: "Ubuntu", "Trebuchet MS", sans-serif;
  }
  * { box-sizing: border-box; margin: 0; padding: 0; }
  html, body {
    width: 1200px; height: 596px; overflow: hidden; background: var(--paper);
  }
  .label-set {
    width: 1200px; height: 596px;
    display: grid;
    grid-template-columns: repeat(4, 1fr);
    grid-template-rows: repeat(2, 1fr);
    gap: 2px;
    background: var(--divider);
  }
  .label {
    position: relative;
    background: var(--paper);
    overflow: hidden;
    font-family: var(--body-font);
    color: var(--ink);
  }
  .label--lime  { --band: var(--lime); }
  .label--olive { --band: var(--olive); }
  .label--rust  { --band: var(--rust); }
  .label--cocoa { --band: var(--cocoa); }

  .label__band {
    position: absolute; left: 0; top: 0;
    width: 100%; height: 150px;
    fill: var(--band);
  }
  .label__slogan {
    position: absolute; left: 0; right: 0; top: 20px;
    text-align: center;
    font-family: var(--headline-font);
    font-weight: 700;
    font-size: 33px;
    line-height: 35px;
    letter-spacing: -1.2px;
    color: var(--paper);
  }
  .label__brand {
    position: absolute;
    right: 12px; top: 126px;
    font-weight: 300;
    font-size: 19px;
    line-height: 19px;
    text-align: center;
    text-transform: uppercase;
    letter-spacing: 0.5px;
    color: var(--brand);
  }
  .label__name {
    position: absolute; left: 14px; top: 186px;
    font-weight: 300;
    font-size: 31px;
    line-height: 31px;
    letter-spacing: -0.6px;
    white-space: nowrap;
  }
  .label__desc {
    position: absolute; left: 15px; right: 40px; top: 223px;
    font-weight: 300;
    font-size: 12.5px;
    line-height: 13px;
    color: var(--muted-ink);
  }
  .label__weight {
    position: absolute; right: 13px; bottom: 10px;
    font-weight: 300;
    font-size: 21px;
    line-height: 24px;
  }

  /* long product name and long description */
  .label--long .label__name { font-size: 27px; letter-spacing: -0.7px; }
  .label--long .label__desc { right: 62px; }

  /* back-row variant: larger brand, name on two lines */
  .label--stacked .label__brand {
    top: 132px; right: 14px;
    font-size: 24px; line-height: 23px;
  }
  .label--stacked .label__name {
    top: 170px;
    font-size: 31px; line-height: 30px;
  }
  .label--stacked.label--long .label__name { font-size: 31px; }
  .label--stacked .label__desc { top: 236px; }
</style>
</head>
<body>
<main class="label-set">

  <!-- top row -->
  <section class="label label--lime">
    <svg class="label__band" viewBox="0 0 300 150" preserveAspectRatio="none" aria-hidden="true">
      <path d="M0 0H300V103L286 105 270 102 250 108 226 104 200 110 172 107 150 113 120 111 96 118 70 116 44 124 22 122 8 132 0 140Z"/>
    </svg>
    <h2 class="label__slogan">Are you<br>Brave Enough?</h2>
    <div class="label__brand">Critter<br>Pantry</div>
    <h1 class="label__name">Zib-A-Lop Tundle</h1>
    <p class="label__desc">A fly shaped chocolate that contains coconut and fly pupae</p>
    <span class="label__weight">100g</span>
  </section>

  <section class="label label--olive">
    <svg class="label__band" viewBox="0 0 300 150" preserveAspectRatio="none" aria-hidden="true">
      <path d="M0 0H300V101L284 104 262 100 240 107 214 103 190 109 164 106 140 112 112 110 88 116 62 114 38 121 16 119 4 128 0 134Z"/>
    </svg>
    <h2 class="label__slogan">Are you<br>Brave Enough?</h2>
    <div class="label__brand">Critter<br>Pantry</div>
    <h1 class="label__name">Plinky Pebbles</h1>
    <p class="label__desc">5 x roasted crickets</p>
    <span class="label__weight">100g</span>
  </section>

  <section class="label label--rust">
    <svg class="label__band" viewBox="0 0 300 150" preserveAspectRatio="none" aria-hidden="true">
      <path d="M0 0H300V102L282 105 262 101 238 108 214 104 188 110 162 107 138 113 110 111 86 117 60 115 36 122 16 120 4 129 0 135Z"/>
    </svg>
    <h2 class="label__slogan">Are you<br>Brave Enough?</h2>
    <div class="label__brand">Critter<br>Pantry</div>
    <h1 class="label__name">Tootle Twirlies</h1>
    <p class="label__desc">5 x roasted mealworms</p>
    <span class="label__weight">100g</span>
  </section>

  <section class="label label--cocoa label--long">
    <svg class="label__band" viewBox="0 0 300 150" preserveAspectRatio="none" aria-hidden="true">
      <path d="M0 0H300V100L284 103 262 99 240 106 214 102 190 108 164 105 140 111 112 109 88 115 62 113 38 120 16 118 4 127 0 133Z"/>
    </svg>
    <h2 class="label__slogan">Are you<br>Brave Enough?</h2>
    <div class="label__brand">Critter<br>Pantry</div>
    <h1 class="label__name">Fudge Dipped Fidgets</h1>
    <p class="label__desc">5 x insects, chocolate coated in milk, white or dark chocolate. Insects include crickets, mealworms and fly pupae</p>
    <span class="label__weight">100g</span>
  </section>

  <!-- bottom row -->
  <section class="label label--lime label--stacked">
    <svg class="label__band" viewBox="0 0 300 150" preserveAspectRatio="none" aria-hidden="true">
      <path d="M0 0H300V103L286 105 270 102 250 108 226 104 200 110 172 107 150 113 120 111 96 118 70 116 44 124 22 122 8 132 0 140Z"/>
    </svg>
    <h2 class="label__slogan">Are you<br>Brave Enough?</h2>
    <div class="label__brand">Critter<br>Pantry</div>
    <h1 class="label__name">Zib-A-Lop<br>Tundle</h1>
    <p class="label__desc">A fly shaped chocolate that contains coconut and fly pupae</p>
    <span class="label__weight">100g</span>
  </section>

  <section class="label label--olive label--stacked">
    <svg class="label__band" viewBox="0 0 300 150" preserveAspectRatio="none" aria-hidden="true">
      <path d="M0 0H300V101L284 104 262 100 240 107 214 103 190 109 164 106 140 112 112 110 88 116 62 114 38 121 16 119 4 128 0 134Z"/>
    </svg>
    <h2 class="label__slogan">Are you<br>Brave Enough?</h2>
    <div class="label__brand">Critter<br>Pantry</div>
    <h1 class="label__name">Plinky<br>Pebbles</h1>
    <p class="label__desc">5 x roasted crickets</p>
    <span class="label__weight">100g</span>
  </section>

  <section class="label label--rust label--stacked">
    <svg class="label__band" viewBox="0 0 300 150" preserveAspectRatio="none" aria-hidden="true">
      <path d="M0 0H300V102L282 105 262 101 238 108 214 104 188 110 162 107 138 113 110 111 86 117 60 115 36 122 16 120 4 129 0 135Z"/>
    </svg>
    <h2 class="label__slogan">Are you<br>Brave Enough?</h2>
    <div class="label__brand">Critter<br>Pantry</div>
    <h1 class="label__name">Tootle<br>Twirlies</h1>
    <p class="label__desc">5 x roasted mealworms</p>
    <span class="label__weight">100g</span>
  </section>

  <section class="label label--cocoa label--stacked label--long">
    <svg class="label__band" viewBox="0 0 300 150" preserveAspectRatio="none" aria-hidden="true">
      <path d="M0 0H300V100L284 103 262 99 240 106 214 102 190 108 164 105 140 111 112 109 88 115 62 113 38 120 16 118 4 127 0 133Z"/>
    </svg>
    <h2 class="label__slogan">Are you<br>Brave Enough?</h2>
    <div class="label__brand">Critter<br>Pantry</div>
    <h1 class="label__name">Fudge<br>Dipped Fidgets</h1>
    <p class="label__desc">5 x insects, chocolate coated in milk, white or dark chocolate. Insects include crickets, mealworms and fly pupae</p>
    <span class="label__weight">100g</span>
  </section>

</main>
</body>
</html>
```